Infographic Customizable and DISC Proof

Design of an infographic used to assist candidates to get an overview on the steps they need to take in order to get the candidate in the best possible position to a new step in their career.

Attached is an outline of the text that needs to be converted to an Infographic.

The infographics will be used predominantly as an attachment in the email from the recruiter to the candidate.

Based on the DISC profile of the candidate we require 2 different designs; 1 designed for yellow disc profiles, stylish, beautifull, with the use of our brand color scheme. And one more factual for example for a blue disc profile with far less or no use of colour and a more sleek clean design.

It is important to take into consideration with your design and format you deliver that we want to be able to change some of the content on the infographics after your delivery completely by ourselves for the following use cases:

1. processes differ per client, hence we must be able to add or remove a step and be able to change the title and body of the steps in order to create an infographic for a different client of ours.
2. We would like to be able to change contact details and the profile picture of the recruiter. Example of a profile picture we would want to use is similar to the profile picture of a workvista profile but then without the background. I attached it as an example for your reference.

It's important to take into consideration that we would need to be able to make such changes by ourselves without the need to become a savvy user of programs such as paint or adobe. The person that would need to be able to make the change is a recruiter, a typical office worker. Please let us know how we would be enabled to do this when you completed the design.

```html
<!DOCTYPE html>
<html lang="nl">
<head>
<meta charset="utf-8">
<title>In 4 stappen optimaal voor het voetlicht</title>
<link rel="stylesheet" href="https://fonts.googleapis.com/css2?family=Archivo+Black&family=Carlito:wght@400;700&display=swap">
<style>
  :root {
    --backdrop: #131b18;
    --paper: #ffffff;
    --band-grey: #dcdedd;
    --brand-orange: #f7941d;
    --brand-blue: #1565a6;
    --heading-blue: #1b6db5;
    --ink: #111111;
  }
  * { box-sizing: border-box; margin: 0; padding: 0; }
  html, body { width: 1200px; height: 768px; overflow: hidden; background: var(--backdrop); }
  body { position: relative; font-family: "Carlito", "Calibri", sans-serif; color: var(--ink); }

  .sheet { position: absolute; left: 350px; top: 34px; width: 500px; height: 689px; background: var(--paper); overflow: hidden; }

  .contact-band { position: absolute; left: 0; top: 12px; width: 500px; height: 70px; background: var(--band-grey); }

  .side-ribbon { position: absolute; left: 26px; top: 12px; width: 106px; height: 526px; }
  .recruiter-photo { position: absolute; left: 33px; top: 50px; width: 88px; height: 88px; border-radius: 50%;
    background: radial-gradient(circle at 50% 40%, #9a8a80 0%, #5b5f6a 60%, #3d4a5c 100%); }

  .contact-item { position: absolute; top: 33px; height: 40px; display: flex; align-items: center; gap: 8px;
    font-weight: 700; font-size: 10px; }
  .contact-item svg { width: 40px; height: 40px; flex: none; }
  .contact-phone { left: 153px; }
  .contact-phone .digits { word-spacing: 9px; }
  .contact-email { left: 330px; }

  .sheet-title { position: absolute; left: 146px; top: 111px; width: 300px; font-family: "Archivo Black", sans-serif;
    font-size: 13.4px; line-height: 19px; color: var(--brand-orange); text-transform: uppercase; }

  .step-heading { position: absolute; left: 148px; font-weight: 700; font-size: 13.5px; line-height: 14px; color: var(--heading-blue); }
  .step-list { position: absolute; left: 146px; list-style: none; font-size: 9.2px; line-height: 12.3px; }
  .step-list li { position: relative; padding-left: 12px; }
  .step-list li::before { content: ""; position: absolute; left: 1px; top: 5px; width: 2.5px; height: 2.5px; border-radius: 50%; background: var(--ink); }

  .support-heading { position: absolute; left: 144px; top: 503px; font-weight: 700; font-size: 13.5px; line-height: 16px; }
  .support-list { position: absolute; left: 144px; top: 527px; list-style: none; font-size: 9.2px; }
  .support-list li { position: relative; padding-left: 26px; height: 20px; line-height: 12px; }
  .support-list li::before { content: ""; position: absolute; left: 0; top: 2px; width: 6px; height: 6px; border-radius: 50%; background: var(--ink); }

  .agency { position: absolute; left: 24px; top: 615px; width: 110px; text-align: center; }
  .agency-name { font-weight: 700; font-size: 23px; line-height: 24px; color: var(--brand-blue); letter-spacing: 0.5px; }
  .agency-tagline { font-size: 8.5px; line-height: 12px; margin-top: 5px; }

  .recruiter-meta { position: absolute; left: 238px; top: 609px; font-size: 9px; line-height: 18.5px; }
</style>
</head>
<body>
  <main class="sheet">
    <div class="contact-band"></div>

    <svg class="side-ribbon" viewBox="0 0 133 657" preserveAspectRatio="none" aria-hidden="true">
      <polygon points="0,0 133,0 133,167 66.5,199 0,167" fill="var(--brand-orange)"/>
      <polygon points="0,167 66.5,199 133,167 133,657 0,657" fill="var(--brand-blue)"/>
    </svg>
    <div class="recruiter-photo" role="img" aria-label="Profielfoto van de recruiter"></div>

    <div class="contact-item contact-phone">
      <svg viewBox="0 0 40 40" aria-hidden="true">
        <circle cx="20" cy="20" r="20" fill="var(--brand-blue)"/>
        <path d="M13 10c1-1 2.5-1 3.3 0l2.4 3c.7.9.6 2.1-.2 2.9l-1.4 1.3c1 2.4 2.7 4.2 5 5.3l1.4-1.4c.8-.8 2-.9 2.9-.2l3 2.4c1 .8 1 2.3 0 3.3l-1.6 1.6c-1.2 1.2-3 1.5-4.5.8C17 25.8 13.2 22 10.8 16.6c-.7-1.5-.4-3.3.8-4.5z" fill="#fff"/>
      </svg>
      <span class="digits">+123 456 7890</span>
    </div>
    <div class="contact-item contact-email">
      <svg viewBox="0 0 40 40" aria-hidden="true">
        <circle cx="20" cy="20" r="20" fill="var(--brand-blue)"/>
        <rect x="10" y="13" width="20" height="14" fill="#fff"/>
        <polyline points="10,13 20,21 30,13" fill="none" stroke="var(--brand-blue)" stroke-width="1.8"/>
      </svg>
      <span>youremail@your.com</span>
    </div>

    <h1 class="sheet-title">In 4 stappen optimaal voor het voetlicht</h1>

    <h2 class="step-heading" style="top:157px">Stap 1: CV voorbereiden</h2>
    <ul class="step-list" style="top:184px">
      <li>Gebruik het bijgevoegde CV-template</li>
      <li>Maximaal 7 pagina's A4</li>
      <li>Schrijf in het Nederlands</li>
      <li>Volg de specifieke datumnotatie [dd-mm-jjjj]</li>
      <li>Vermeld uren per week bij elke functie in het werkverleden</li>
      <li>Voeg blokken toe waar nodig</li>
    </ul>

    <h2 class="step-heading" style="top:271px">Stap 2: Eisen en wensen beargumenteren</h2>
    <ul class="step-list" style="top:297px">
      <li>Beargumenteer eisen beknopt en herleidbaar</li>
      <li>Beargumenteer wensen uitgebreid en kwalitatief</li>
      <li>Geef situatieschetsen en voorbeelden van ervaring</li>
      <li>Vermeld het aantal maanden ervaring per gevraagd element</li>
    </ul>

    <h2 class="step-heading" style="top:359px">Stap 3: Motivatie en introductie</h2>
    <ul class="step-list" style="top:386px">
      <li>Schrijf een korte, persoonlijke introductie</li>
      <li>Benadruk jouw kracht en motivatie voor de rol en de organisatie</li>
    </ul>

    <h2 class="step-heading" style="top:424px">Stap 4: Controleer en verstuur</h2>
    <ul class="step-list" style="top:451px">
      <li>Controleer alle documenten op volledigheid en nauwkeurigheid</li>
      <li>Verstuur je CV, beargumentatie en motivatie per e-mail</li>
      <li>Bevestig de financiële aanbieding per e-mail</li>
    </ul>

    <h3 class="support-heading">Extra ondersteuning</h3>
    <ul class="support-list">
      <li>Neem contact op met je toegewezen contactpersoon voor vragen</li>
      <li>Raadpleeg bijgevoegde voorbeeld beargumentatie</li>
    </ul>

    <div class="agency">
      <div class="agency-name">VELTRION</div>
      <div class="agency-tagline">Ruimte voor Groei</div>
    </div>

    <div class="recruiter-meta">
      <p>Profielfoto Recruiter</p>
      <p>Tel / E-mail</p>
    </div>
  </main>
</body>
</html>
```